Professional Website

We are looking for a new website for our Staffing Company. Attached is a document with all the details and pages needed along with some examples of others websites.

We want a professional Look and feel around the same color theme as the attached Vivid Vision.

We currently host our site on SiteKarn.io. If the winning designer can also add to SiteKarn, that is a plus.

```html
<!DOCTYPE html>
<html lang="en">
<head>
<meta charset="utf-8">
<title>HireBridge – Clerical &amp; Industrial Staffing</title>
<link href="https://fonts.googleapis.com/css2?family=Poppins:ital,wght@0,400;0,600;0,700;1,400&display=swap" rel="stylesheet">
<style>
:root{
  --royal:#1224a0;
  --royal-deep:#0c1c8e;
  --royal-bright:#2a42b8;
  --charcoal:#454545;
  --ink:#111318;
  --heading-blue:#1628a0;
  --body-text:#444;
  --white:#fff;
  --muted:#9ea3b3;
}
*{margin:0;padding:0;box-sizing:border-box}
html,body{width:932px;height:1200px;overflow:hidden}
body{font-family:'Poppins',sans-serif;background:var(--white);position:relative}
.page{position:relative;width:932px;height:1200px}
.bg-shapes{position:absolute;inset:0}
.brand{position:absolute;left:64px;top:22px;color:var(--white)}
.brand-name{font-weight:700;font-size:34px;letter-spacing:-1px;line-height:1}
.brand-tag{font-weight:400;font-size:8.5px;letter-spacing:1px;margin-top:3px}
.top-nav{position:absolute;left:341px;top:38px;height:32px}
.nav-item{position:absolute;top:0;height:32px;display:flex;align-items:center;justify-content:center;color:var(--white);font-weight:700;font-size:9.5px;text-decoration:none}
.nav-item svg{position:absolute;inset:0}
.nav-item span{position:relative}
.hero-title{position:absolute;left:103px;top:208px;color:var(--white);font-weight:700;font-size:41px;line-height:48px}
.btn{position:absolute;width:232px;height:48px;border:1.5px solid var(--white);border-radius:24px;display:flex;align-items:center;justify-content:center;color:var(--white);font-weight:700;font-size:16px;text-decoration:none}
.btn-job{left:98px;top:322px;background:var(--charcoal)}
.btn-hire{left:96px;top:385px;background:var(--royal-bright)}
.hero-art{position:absolute;left:388px;top:115px;width:462px;height:385px;border-radius:46% 54% 40% 60%/52% 45% 55% 48%;background:radial-gradient(circle at 60% 45%,#e4e4f6 0%,#c9c8ec 45%,rgba(201,200,236,0) 72%)}
.about-title{position:absolute;left:113px;top:668px;color:var(--heading-blue);font-weight:700;font-size:29px}
.about-text{position:absolute;left:115px;top:722px;width:432px;color:var(--body-text);font-style:italic;font-size:12.4px;line-height:22.8px}
.about-photo{position:absolute;left:564px;top:660px;width:262px;height:262px;border-radius:50%;background:radial-gradient(circle at 35% 60%,#b07a55 0%,#5a6f8c 45%,#2b3a5a 100%)}
.footer-title{position:absolute;color:var(--white);font-weight:700;font-size:16px}
.areas-title{left:141px;top:1055px}
.areas{position:absolute;left:141px;top:1089px;display:flex;gap:29px;list-style:none;color:var(--muted);font-weight:600;font-size:13px}
.areas li{display:flex;align-items:center;gap:5px}
.areas li::before{content:"";width:8px;height:8px;border-radius:50%;background:#3a4fb8;border:1px solid var(--muted)}
.phone-badge{position:absolute;left:555px;top:1058px;width:48px;height:48px;border-radius:50%;background:var(--royal-bright);border:2px solid var(--white);display:flex;align-items:center;justify-content:center}
.hotline-title{left:617px;top:1055px}
.hotline-number{position:absolute;left:613px;top:1080px;color:var(--white);font-weight:700;font-size:22px}
.footer-rule{position:absolute;left:141px;top:1136px;width:649px;height:1px;background:rgba(255,255,255,.15)}
.copyright{position:absolute;left:0;width:932px;top:1157px;text-align:center;color:#d8d8e0;font-size:11px}
</style>
</head>
<body>
<div class="page">
  <svg class="bg-shapes" width="932" height="1200" viewBox="0 0 932 1200">
    <defs>
      <linearGradient id="heroBlue" x1="0" y1="0" x2="1" y2="1">
        <stop offset="0" stop-color="#1428a6"/><stop offset="1" stop-color="#0c1c8e"/>
      </linearGradient>
      <linearGradient id="footerShade" x1="0" y1="0" x2="0" y2="1">
        <stop offset="0" stop-color="#24262e"/><stop offset="1" stop-color="#0b0c12"/>
      </linearGradient>
    </defs>
    <polygon points="0,0 932,0 932,466 370,545 0,595" fill="url(#heroBlue)"/>
    <polygon points="370,545 932,466 932,612" fill="var(--charcoal)"/>
    <polygon points="0,935 430,993 0,1028" fill="var(--royal-bright)"/>
    <polygon points="0,1028 932,955 932,1200 0,1200" fill="url(#footerShade)" role="img" aria-label="Dimmed photo of a busy city crowd at dusk"/>
  </svg>

  <header>
    <div class="brand">
      <div class="brand-name">HireBridge</div>
      <div class="brand-tag">CLERICAL &amp; INDUSTRIAL</div>
    </div>
    <nav class="top-nav">
      <a class="nav-item" href="#" style="left:0;width:126px"><svg width="126" height="32"><polygon points="0.75,0.75 113,0.75 125,16 113,31.25 0.75,31.25" fill="none" stroke="#fff" stroke-width="1.2"/></svg><span>EMPLOYEE LOGIN</span></a>
      <a class="nav-item" href="#" style="left:122px;width:130px"><svg width="130" height="32"><polygon points="0.75,0.75 117,0.75 129,16 117,31.25 0.75,31.25 12,16" fill="none" stroke="#fff" stroke-width="1.2"/></svg><span>QUICKPAY CARD LOGIN</span></a>
      <a class="nav-item" href="#" style="left:248px;width:128px"><svg width="128" height="32"><polygon points="0.75,0.75 115,0.75 127,16 115,31.25 0.75,31.25 12,16" fill="none" stroke="#fff" stroke-width="1.2"/></svg><span>LAKESHORE BANK LOGIN</span></a>
      <a class="nav-item" href="#" style="left:372px;width:174px"><svg width="174" height="32"><polygon points="0.75,0.75 161,0.75 173,16 161,31.25 0.75,31.25 12,16" fill="none" stroke="#fff" stroke-width="1.2"/></svg><span>HOTLINE # 312-555-0148</span></a>
    </nav>
  </header>

  <section class="hero">
    <h1 class="hero-title">Welcome to<br>HireBridge</h1>
    <a class="btn btn-job" href="#">I’M LOOKING FOR A JOB</a>
    <a class="btn btn-hire" href="#">I NEED EMPLOYEES</a>
    <div class="hero-art" role="img" aria-label="Illustration of recruiters reviewing candidate profiles on a large laptop with a megaphone"></div>
  </section>

  <section class="about">
    <h2 class="about-title">About us</h2>
    <p class="about-text">Greatest part of our daily job is that we are constantly bringing people together. Our Clients come to us in search of the perfect candidate and the job hunters approach us when they are in need of a job or looking for their next exciting role. Being able to work with and connect the two is incredibly satisfying. Not to mention that in today's current job market, employers are fighting for the top talent. This makes our employees and partners grateful for the help in finding it!</p>
    <div class="about-photo" role="img" aria-label="Photo of hands reviewing and signing a document"></div>
  </section>

  <footer>
    <h3 class="footer-title areas-title">Areas we service</h3>
    <ul class="areas"><li>Blue Island</li><li>Alsip</li><li>Romeoville</li></ul>
    <div class="phone-badge">
      <svg width="24" height="24" viewBox="0 0 24 24"><path d="M6.6 10.8c1.4 2.8 3.8 5.1 6.6 6.6l2.2-2.2c.3-.3.7-.4 1-.2 1.1.4 2.3.6 3.6.6.6 0 1 .4 1 1V20c0 .6-.4 1-1 1C10.6 21 3 13.4 3 4c0-.6.4-1 1-1h3.5c.6 0 1 .4 1 1 0 1.3.2 2.5.6 3.6.1.3 0 .7-.2 1z" fill="#fff"/></svg>
    </div>
    <h3 class="footer-title hotline-title">Hotline</h3>
    <div class="hotline-number"># 312-555-0148</div>
    <div class="footer-rule"></div>
    <p class="copyright">© Copyright 2022 All Rights Reserved.</p>
  </footer>
</div>
</body>
</html>
```